Website Design for Employee Moral and Happiness Company

Looking for a clean website design that explains our features in a step by step manner so our visitors know exactly what our site does before logging in.

The site is called "Velasto". See logo design and video for a sample of style and an overview of what we do.

Target Market(s)

Business owners that are looking to retain employees.

Number of Pages Required

1 page

```html
<!DOCTYPE html>
<html lang="en">
<head>
<meta charset="utf-8">
<title>Velasto — Employee Morale</title>
<link rel="stylesheet" href="https://fonts.googleapis.com/css2?family=Libre+Baskerville:wght@700&family=Montserrat:wght@500;600&display=swap">
<style>
  :root {
    --orange: #ff6600;
    --orange-light: #ff9a5a;
    --orange-deep: #c94f0a;
    --black: #000000;
    --white: #ffffff;
    --blue: #559cff;
    --ink: #111111;
    --yellow: #ffd24a;
  }
  * { margin: 0; padding: 0; box-sizing: border-box; }
  html, body { width: 1200px; height: 876px; overflow: hidden; background: var(--white); }
  body { font-family: "Montserrat", sans-serif; position: relative; }
  .backdrop { position: absolute; left: 0; top: 0; width: 1200px; height: 876px; }
  .topbar {
    position: absolute; left: 0; top: 0; width: 1200px; height: 42.5px;
    background: var(--black); color: var(--white);
    font-size: 11.5px; font-weight: 600; letter-spacing: 0.4px;
  }
  .topbar .booking { position: absolute; left: 159px; top: 14px; }
  .topbar .booking a { color: var(--white); text-decoration: underline; text-underline-offset: 3px; }
  .social { position: absolute; top: 16px; width: 10px; height: 10px; border-radius: 50%; background: var(--white); }
  .brand {
    position: absolute; left: 159px; top: 70px;
    font-family: "Libre Baskerville", serif; font-weight: 700; font-size: 40px;
    color: var(--ink); letter-spacing: -0.5px;
  }
  .nav { position: absolute; top: 96px; font-size: 11px; font-weight: 600; color: var(--ink); }
  .contact-btn {
    position: absolute; left: 881px; top: 81px; width: 148px; height: 43px;
    background: var(--blue); color: var(--white); font-size: 11px; font-weight: 600;
    display: flex; align-items: center; justify-content: center;
    box-shadow: 3px 3px 0 var(--white);
  }
  .headline {
    position: absolute; left: 159px; top: 215px;
    font-family: "Libre Baskerville", serif; font-weight: 700; font-size: 59px;
    line-height: 69px; color: var(--white); letter-spacing: -0.5px;
  }
  .intro {
    position: absolute; left: 159px; top: 450px; width: 420px;
    font-size: 11.3px; font-weight: 500; line-height: 18.75px; color: var(--white);
  }
  .learn-btn {
    position: absolute; left: 159px; top: 532px; width: 147px; height: 42px;
    background: var(--black); color: var(--white); font-size: 11px; font-weight: 600;
    display: flex; align-items: center; justify-content: center;
    box-shadow: 3px 3px 0 var(--white);
  }
  .hero-art {
    position: absolute; left: 600px; top: 166px; width: 519px; height: 450px;
    border-radius: 40px;
    background: radial-gradient(ellipse at 55% 40%, #f0a060 0%, #e07a2a 45%, rgba(255,102,0,0) 75%);
  }
  .dots-top { position: absolute; left: 1011px; top: 176px; width: 180px; height: 48px; background: var(--orange-deep); opacity: 0.25; border-radius: 4px; }
  .dots-bottom { position: absolute; left: 0; top: 599px; width: 68px; height: 72px; background: var(--yellow); opacity: 0.35; border-radius: 4px; }
  .section-title {
    position: absolute; left: 0; top: 764px; width: 1200px; text-align: center;
    font-family: "Libre Baskerville", serif; font-weight: 700; font-size: 38px; color: var(--ink);
  }
</style>
</head>
<body>
  <svg class="backdrop" viewBox="0 0 1920 1404" preserveAspectRatio="none" aria-hidden="true">
    <path fill="var(--orange)" d="M0,68 H1920 V830 C1750,770 1560,780 1420,880 C1200,1040 1000,1150 800,1145 C600,1140 420,940 250,945 C120,950 40,1030 0,1085 Z"/>
    <path fill="var(--orange-light)" d="M0,68 H1040 C1000,150 900,200 760,210 C600,220 500,300 400,380 C300,460 200,520 80,525 C40,525 0,515 0,515 Z"/>
  </svg>

  <header class="topbar">
    <p class="booking">To Book an Event! <a href="#">CLICK HERE</a></p>
    <span class="social" style="left:921px" aria-label="Social link"></span>
    <span class="social" style="left:991px" aria-label="Social link"></span>
    <span class="social" style="left:1028px" aria-label="Social link"></span>
  </header>

  <div class="brand">Velasto</div>

  <nav>
    <span class="nav" style="left:454px">HOME</span>
    <span class="nav" style="left:530px">ABOUT US</span>
    <span class="nav" style="left:629px">SERVICES</span>
    <span class="nav" style="left:724px">EVENTS</span>
    <span class="nav" style="left:809px">TEAM</span>
    <a class="contact-btn" href="#">CONTACT US</a>
  </nav>

  <div class="dots-top" role="img" aria-label="Decorative dot grid"></div>
  <div class="dots-bottom" role="img" aria-label="Decorative dot grid"></div>

  <h1 class="headline">Helping your<br>EMPLOYEE to<br>Boost Moral</h1>
  <p class="intro">Lorem ipsum dolor sit amet, consectetur adipisicing elit, sed do eiusmod tempor incididunt ut labore et dolore magna aliqua. Ut enim ad minim veniam, quis nostrud exercitation ullamco laboris nisi.</p>
  <a class="learn-btn" href="#">LEARN MORE</a>

  <div class="hero-art" role="img" aria-label="Illustration of a friendly robot lifting the mood of two office workers at their desks"></div>

  <h2 class="section-title">How we can help?</h2>
</body>
</html>
```